Help keep hoosiers happy and at home!

We need a billboard designed for our Indiana based healthcare business called 'Harbor Lane Home Aides'. We administer a medicaid waiver program that provides support and financial aid to live in caregivers that take care of someone who would otherwise be in a nursing home or skilled nursing facility. Qualified caregivers could be eligible to receive up to 1200 dollars a month in tax free financial aid, as well as access to nursing support that helps manage any unexpected situations or changes in a care recipients condition or care routine. Our program empowers families to keep their loved ones at home and out of the nursing home. NOTE: We believe the tagline at the bottom of our logo is disproportionately small. We would like to see that tagline larger and easier to read. I look forward to seeing your design ideas!

Target Market(s)

Medicaid aged beneficiaries and caregivers.

Industry/Entity Type

Home Healthcare

Colors
0054AA
0677BA
7BADD7
CADEEF
E8F1F8

Requirements
Nice to have
• "Empowering friends and family to care for their loves ones at home. Eligible participants receive up to $15,000 a year, tax free."

```html
<!DOCTYPE html>
<html lang="en">
<head>
<meta charset="UTF-8">
<title>Harbor Lane Home Aides – Billboard</title>
<link rel="stylesheet" href="https://fonts.googleapis.com/css2?family=Tinos&display=swap">
<style>
  :root {
    --blue-deep: #0054AA;
    --blue-mid: #0677BA;
    --blue-soft: #7BADD7;
    --blue-pale: #CADEEF;
    --blue-mist: #E8F1F8;
    --paper: #eef0f2;
    --ink: #45508f;
    --white: #ffffff;
  }
  * { margin: 0; padding: 0; box-sizing: border-box; }
  html, body { width: 1200px; height: 801px; overflow: hidden; background: var(--paper); }
  .billboard {
    position: relative;
    width: 1200px;
    height: 801px;
    background: var(--paper);
    overflow: hidden;
  }
  .billboard__waves { position: absolute; inset: 0; }
  .brand-name {
    position: absolute;
    left: 130px;
    top: 310px;
    width: 600px;
    text-align: center;
    font-family: "Tinos", serif;
    font-weight: 400;
    font-size: 50px;
    line-height: 1.1;
    color: var(--ink);
    white-space: nowrap;
  }
  .message {
    position: absolute;
    left: 80px;
    top: 432px;
    width: 660px;
    text-align: center;
    font-family: "Tinos", serif;
    font-size: 33px;
    line-height: 1.38;
    color: var(--ink);
    white-space: nowrap;
  }
  .photo {
    position: absolute;
    left: 765px;
    top: 190px;
    width: 440px;
    height: 440px;
    border-radius: 50%;
    background: radial-gradient(circle at 45% 40%, #f1e6dc 0%, #d9cfc6 40%, #b9c3cc 75%, #8fb4d4 100%);
  }
</style>
</head>
<body>
  <main class="billboard">
    <svg class="billboard__waves" width="1200" height="801" viewBox="0 0 1200 801" aria-hidden="true">
      <path d="M420 0 C560 40 700 95 860 95 C980 95 1100 40 1200 10 L1200 0 Z" fill="var(--blue-soft)"/>
      <path d="M470 0 C600 35 720 80 860 80 C980 80 1100 30 1200 0 Z" fill="var(--blue-mid)"/>
      <path d="M560 0 C660 25 760 55 870 55 C990 55 1100 20 1200 0 Z" fill="var(--blue-deep)"/>
      <g fill="var(--white)">
        <circle cx="590" cy="55" r="3"/><circle cx="612" cy="58" r="3"/><circle cx="634" cy="61" r="3"/>
        <circle cx="656" cy="64" r="3"/><circle cx="678" cy="67" r="3"/><circle cx="700" cy="70" r="3"/>
        <circle cx="722" cy="72" r="3"/>
      </g>
      <circle cx="1150" cy="150" r="11" fill="none" stroke="var(--blue-mid)" stroke-width="2"/>

      <circle cx="985" cy="410" r="238" fill="none" stroke="var(--blue-soft)" stroke-width="1.5"/>

      <path d="M0 535 C160 520 330 600 500 670 C660 735 860 750 1000 680 C1090 635 1150 580 1200 545 L1200 801 L0 801 Z" fill="var(--blue-mid)"/>
      <path d="M0 600 C150 600 320 665 500 720 C680 775 880 770 1020 700 C1100 660 1160 620 1200 595 L1200 801 L0 801 Z" fill="var(--blue-deep)"/>
      <g fill="var(--white)">
        <circle cx="35" cy="720" r="3.5"/><circle cx="62" cy="719" r="3.5"/><circle cx="89" cy="718" r="3.5"/><circle cx="116" cy="717" r="3.5"/><circle cx="143" cy="716" r="3.5"/><circle cx="170" cy="715" r="3.5"/><circle cx="197" cy="714" r="3.5"/>
        <circle cx="35" cy="745" r="3.5"/><circle cx="62" cy="744" r="3.5"/><circle cx="89" cy="743" r="3.5"/><circle cx="116" cy="742" r="3.5"/><circle cx="143" cy="741" r="3.5"/><circle cx="170" cy="740" r="3.5"/><circle cx="197" cy="739" r="3.5"/>
        <circle cx="35" cy="770" r="3.5"/><circle cx="62" cy="769" r="3.5"/><circle cx="89" cy="768" r="3.5"/><circle cx="116" cy="767" r="3.5"/><circle cx="143" cy="766" r="3.5"/><circle cx="170" cy="765" r="3.5"/><circle cx="197" cy="764" r="3.5"/>
      </g>
      <circle cx="375" cy="690" r="8" fill="none" stroke="var(--blue-pale)" stroke-width="2"/>
    </svg>

    <div class="brand-name">Harbor Lane Home Aides</div>

    <p class="message">Empowering friends and family to care for their<br>loves ones at home. Eligible participants receive<br>up to $15,000 a year, tax free.</p>

    <div class="photo" role="img" aria-label="Photo of a smiling young woman exercising on a mat with two little girls, one holding a small dumbbell"></div>
  </main>
</body>
</html>
```